Texas-Based Roofing Company Looking for Creative Billboard Design

We need a billboard designed for a roofing company in the Dallas - Fort Worth area. They are a tech-forward company that uses drone technology to complete roof inspections. We would like to see a design that is out-of-the-box in terms of creativity. It can be marketed towards a hail/wind storm event, or a creative approach to helping customers think of VORTANIC when it comes to roofing needs.
Updates

Low design quality

Target Market(s)

residential homeowners

Industry/Entity Type

Roofing

Requirements
Must have
• Creative approach or play on words to elevate brand awareness.

```html
<!DOCTYPE html>
<html lang="en">
<head>
<meta charset="utf-8">
<title>Vortanic Roofing Billboard</title>
<link href="https://fonts.googleapis.com/css2?family=Montserrat:wght@400;500;800;900&display=swap" rel="stylesheet">
<style>
  :root {
    --gold: #e3ab2b;
    --navy: #1f4479;
    --ink: #232323;
    --white: #ffffff;
    --page: #f2f2f2;
  }
  html, body {
    margin: 0;
    padding: 0;
    width: 1200px;
    height: 1089px;
    overflow: hidden;
    background: var(--page);
  }
  .canvas {
    position: relative;
    width: 1200px;
    height: 1089px;
  }
  .billboard {
    position: absolute;
    left: 0;
    top: 370px;
    width: 1500px;
    height: 437px;
    transform: scale(0.8);
    transform-origin: 0 0;
    background: var(--white);
    overflow: hidden;
    font-family: "Montserrat", sans-serif;
  }
  .billboard-shapes {
    position: absolute;
    inset: 0;
  }
  .headline {
    position: absolute;
    left: 34px;
    top: 18px;
    margin: 0;
    font-weight: 900;
    color: var(--gold);
    text-transform: uppercase;
    line-height: 0.92;
    text-shadow: 3px 3px 0 #1a1a1a, -1px -1px 0 #1a1a1a, 1px -1px 0 #1a1a1a, -1px 1px 0 #1a1a1a;
  }
  .headline-lead {
    display: block;
    font-size: 46px;
    letter-spacing: -0.5px;
  }
  .headline-main {
    display: block;
    font-size: 82px;
    letter-spacing: 1px;
  }
  .partner-badge {
    position: absolute;
    left: 25px;
    top: 362px;
    width: 58px;
    height: 58px;
    border-radius: 9px;
    background: var(--white);
  }
  .brand {
    position: absolute;
    right: 32px;
    top: 112px;
    text-align: right;
  }
  .brand-name {
    margin: 0;
    font-size: 50px;
    font-weight: 500;
    color: var(--ink);
    letter-spacing: 2.5px;
    line-height: 1;
  }
  .brand-tagline {
    margin: 12px 0 0;
    font-size: 16.5px;
    font-weight: 500;
    color: var(--gold);
    letter-spacing: 3.6px;
  }
  .services {
    position: absolute;
    right: 30px;
    top: 222px;
    margin: 0;
    padding: 0;
    list-style: none;
    text-align: right;
    font-weight: 800;
    font-size: 25px;
    letter-spacing: 2.4px;
    line-height: 33px;
    color: var(--gold);
  }
  .services-title {
    color: var(--white);
  }
</style>
</head>
<body>
<div class="canvas">
  <section class="billboard">
    <svg class="billboard-shapes" width="1500" height="437" viewBox="0 0 1500 437">
      <defs>
        <linearGradient id="photoTone" x1="0" y1="0" x2="0" y2="1">
          <stop offset="0" stop-color="#d9dcdc"/>
          <stop offset="0.45" stop-color="#a9ad9f"/>
          <stop offset="0.7" stop-color="#5e7a48"/>
          <stop offset="1" stop-color="#3a4e2c"/>
        </linearGradient>
      </defs>
      <polygon role="img" aria-label="Photo of roofers in safety vests and hard hats working on a steel roof frame" points="0,0 790,0 1000,437 0,437" fill="url(#photoTone)"/>
      <polygon class="accent-stripe" points="790,0 815,0 1025,437 1000,437" fill="var(--gold)"/>
      <polygon class="services-band" points="906,205 1500,205 1500,437 1015,437" fill="var(--navy)"/>
    </svg>

    <h1 class="headline">
      <span class="headline-lead">Best Choice For</span>
      <span class="headline-main">Roofing</span>
      <span class="headline-main">Services</span>
    </h1>

    <div class="partner-badge"></div>

    <div class="brand">
      <p class="brand-name">VORTANIC ROOFING</p>
      <p class="brand-tagline">BUILDING THE KINGDOM ONE ROOF AT A TIME</p>
    </div>

    <ul class="services">
      <li class="services-title">SERVICES:</li>
      <li>RESIDENTIAL ROOFING</li>
      <li>COMMERCIAL ROOFING</li>
      <li>PAINTING | ELECTRICAL</li>
      <li>CONCIERGE VIP SERVICES</li>
      <li>FOR REALTORS</li>
    </ul>
  </section>
</div>
</body>
</html>
```